Business Card Design for Vantor Gear

We want to have a business card design for our company.
Company website: www.vantorgear-example.com.au
We looking for something cool, funky, and impressive, yet elegant.
Below are the contents that should be displayed on the card:
Front:
Name: Mark Dellow
Title: Sales & Purchasing
Company Name: Vantor Gear Pty Ltd
Phone: 02 5550 1473
Mobile: 0400 555 019
Email: mark@vantorgear-example.com.au
Website: www.vantorgear-example.com.au
Address: 17 Brackley St
Lidcombe, NSW 2141
Back:
We buy sell new used Norvex and network equipment
• Huge Savings - save up to 95% off list prices
• Highest Reliability
• Comprehensive Warranty
• Fast delivery
• Large range of hardware in stock
Our logo can be downloaded at: www.vantorgear-example.com.au/logo.zip

```html
<!DOCTYPE html>
<html lang="en">
<head>
<meta charset="utf-8">
<title>Vantor Gear — Business Card</title>
<link rel="stylesheet" href="https://fonts.googleapis.com/css2?family=Arimo:ital,wght@0,400;0,700;1,700&display=swap">
<style>
  :root {
    --bg: #d9dadc;
    --paper: #ffffff;
    --blue-deep: #0a3fa8;
    --blue-mid: #1567d3;
    --blue-light: #36a6ee;
    --ink-blue: #0b3f9c;
    --ink-white: #ffffff;
  }
  * { margin: 0; padding: 0; box-sizing: border-box; }
  html, body { width: 1200px; height: 800px; overflow: hidden; }
  body {
    background: var(--bg);
    font-family: "Arimo", Arial, sans-serif;
    position: relative;
  }
  .card {
    position: absolute;
    left: 300px;
    width: 600px;
    height: 345px;
    background: var(--paper);
    overflow: hidden;
    box-shadow: 0 6px 18px rgba(0,0,0,0.18);
  }
  .card--front { top: 30px; }
  .card--back { top: 415px; }
  .card__wave { position: absolute; inset: 0; width: 100%; height: 100%; }

  .brand {
    position: absolute;
    left: 40px; top: 44px;
    display: flex; align-items: center; gap: 10px;
  }
  .brand__dot {
    width: 26px; height: 26px; border-radius: 50%;
    background: var(--blue-mid);
  }
  .brand__name {
    font-weight: 700; font-size: 26px; color: var(--ink-blue);
  }
  .person { position: absolute; left: 40px; top: 112px; color: var(--ink-blue); }
  .person__name { font-weight: 700; font-size: 30px; }
  .person__title { font-weight: 700; font-style: italic; font-size: 16px; margin-top: 4px; letter-spacing: 0.5px; }

  .contacts {
    position: absolute; right: 28px; top: 130px;
    list-style: none; color: var(--ink-white); font-size: 14px;
  }
  .contacts li {
    display: flex; align-items: center; justify-content: flex-end;
    gap: 10px; height: 26px; white-space: nowrap;
  }
  .contacts svg { width: 18px; height: 18px; flex: none; }

  .pitch {
    position: absolute; left: 40px; top: 148px;
    color: var(--ink-white); font-size: 15px; line-height: 1.5;
  }
  .pitch__lead { margin-bottom: 6px; }
  .pitch ul { list-style: none; }
  .pitch li::before { content: "- "; }
  .brand--back { left: auto; right: 36px; top: 28px; }
  .brand--back .brand__name { font-size: 20px; }
  .brand--back .brand__dot { width: 20px; height: 20px; }
</style>
</head>
<body>

<section class="card card--front" aria-label="Business card front">
  <svg class="card__wave" viewBox="0 0 600 345" preserveAspectRatio="none" aria-hidden="true">
    <defs>
      <linearGradient id="frontBlue" x1="0" y1="1" x2="1" y2="0">
        <stop offset="0" stop-color="#0a3fa8"/>
        <stop offset="0.55" stop-color="#1a7fe0"/>
        <stop offset="1" stop-color="#0d4fbf"/>
      </linearGradient>
    </defs>
    <path d="M130 345 C230 300 280 220 330 140 C390 50 500 15 600 0 L600 345 Z" fill="url(#frontBlue)"/>
    <path d="M0 0 L250 0 C180 18 120 22 60 15 C30 12 10 6 0 4 Z" fill="url(#frontBlue)"/>
  </svg>

  <div class="brand">
    <span class="brand__dot"></span>
    <span class="brand__name">Vantor Gear</span>
  </div>
  <div class="person">
    <p class="person__name">Mark Dellow</p>
    <p class="person__title">Sales &amp; Purchasing</p>
  </div>

  <ul class="contacts">
    <li>
      <svg viewBox="0 0 24 24" fill="#fff"><path d="M6.6 10.8a15 15 0 006.6 6.6l2.2-2.2a1 1 0 011-.25 11 11 0 003.6.6 1 1 0 011 1V20a1 1 0 01-1 1A17 17 0 013 4a1 1 0 011-1h3.5a1 1 0 011 1 11 11 0 00.6 3.6 1 1 0 01-.25 1z"/></svg>
      <span>02 5550 1473</span>
    </li>
    <li>
      <svg viewBox="0 0 24 24" fill="none" stroke="#fff" stroke-width="2"><rect x="7" y="2" width="10" height="20" rx="2"/><line x1="11" y1="18" x2="13" y2="18"/></svg>
      <span>0400 555 019</span>
    </li>
    <li>
      <svg viewBox="0 0 24 24" fill="#fff"><rect x="2" y="6" width="9" height="16"/><rect x="13" y="2" width="9" height="20"/></svg>
      <span>17 Brackley St Lidcombe, NSW 2141</span>
    </li>
    <li>
      <svg viewBox="0 0 24 24" fill="none" stroke="#fff" stroke-width="2"><rect x="2" y="5" width="20" height="14"/><polyline points="2,5 12,13 22,5"/></svg>
      <span>mark@vantorgear-example.com.au</span>
    </li>
    <li>
      <svg viewBox="0 0 24 24" fill="none" stroke="#fff" stroke-width="1.8"><circle cx="12" cy="12" r="10"/><ellipse cx="12" cy="12" rx="4" ry="10"/><line x1="2" y1="12" x2="22" y2="12"/></svg>
      <span>www.vantorgear-example.com.au</span>
    </li>
  </ul>
</section>

<section class="card card--back" aria-label="Business card back">
  <svg class="card__wave" viewBox="0 0 600 345" preserveAspectRatio="none" aria-hidden="true">
    <defs>
      <linearGradient id="backBlue" x1="0" y1="0" x2="1" y2="1">
        <stop offset="0" stop-color="#1d8be6"/>
        <stop offset="0.6" stop-color="#1567d3"/>
        <stop offset="1" stop-color="#0a3fa8"/>
      </linearGradient>
    </defs>
    <path d="M0 110 C150 75 330 70 600 115 L600 230 C520 260 470 300 440 345 L0 345 Z" fill="url(#backBlue)"/>
  </svg>

  <div class="brand brand--back">
    <span class="brand__dot"></span>
    <span class="brand__name">Vantor Gear</span>
  </div>

  <div class="pitch">
    <p class="pitch__lead">We buy sell new used Norvex and network equipment</p>
    <ul>
      <li>Huge Savings - save up to 95% off list prices</li>
      <li>Highest Reliability</li>
      <li>Comprehensive Warranty</li>
      <li>Fast delivery</li>
      <li>Large range of hardware in stock</li>
    </ul>
  </div>
</section>

</body>
</html>
```